Business Card Design - R.T. Custom Cabinets Ltd.

Design a business card, including a new logo for a new company in Vancouver, British Columbia, Canada.

The logo must be available as a separate file.

The card should include all company information including:
R.T. Custom Cabinets Ltd.
5826 Larkspur Avenue
Burnaby, B.C. V7K 2P9
Telehone: 604-555-0173
Fax: 604-555-0173
www.rtcustomcabinets.example

As well as individual contact information for employees:
Name
Position
Telephone
Email

The card must include a thoughtful message as well

Target Market(s)

Custom Cabinets

Industry/Entity Type

Business

Contact Information for Business Card

Important information on the front, thoughtful message on the back

Colors
fbed22
9bcb3c
0355a3
ec1f27

Requirements
Must have
• See project description
Nice to have
• images that showcase custom cabinets (european, modern and traditional) styles

```html
<!DOCTYPE html>
<html lang="en">
<head>
<meta charset="utf-8">
<title>R.T. Custom Cabinets Ltd. – Business Card</title>
<link rel="stylesheet" href="https://fonts.googleapis.com/css2?family=Open+Sans:wght@400;600;700&display=swap">
<style>
  :root {
    --stage: #a7a8ad;
    --wood-light: #e0a660;
    --wood-mid: #c9843d;
    --wood-dark: #9c5f24;
    --ink: #1a120c;
    --card-dark: #2a160d;
    --card-dark-edge: #1a0c06;
    --tan: #d9ae7c;
    --tan-soft: #c99c6a;
  }
  * { box-sizing: border-box; margin: 0; padding: 0; }
  html, body {
    width: 1200px; height: 863px; overflow: hidden;
    background: var(--stage);
    font-family: "Open Sans", Arial, sans-serif;
  }
  .stage { position: relative; width: 1200px; height: 863px; }
  .card {
    position: absolute; width: 580px; height: 331px;
    box-shadow: 0 12px 28px rgba(0,0,0,.35);
  }
  .card--front {
    left: 470px; top: 40px;
    background: linear-gradient(100deg, var(--wood-mid) 0%, var(--wood-light) 35%, var(--wood-mid) 60%, var(--wood-light) 80%, var(--wood-dark) 100%);
  }
  .card--back {
    left: 150px; top: 470px;
    background: radial-gradient(ellipse at 60% 40%, #3b2114 0%, var(--card-dark) 55%, var(--card-dark-edge) 100%);
    color: var(--tan);
  }
  .brand {
    position: absolute; display: flex; align-items: center; gap: 12px;
    font-weight: 700; font-size: 28px; white-space: nowrap;
  }
  .brand__dot { width: 26px; height: 26px; border-radius: 50%; flex: none; }
  .card--front .brand { left: 50%; top: 50%; transform: translate(-50%, -50%); color: var(--ink); }
  .card--front .brand__dot { background: var(--ink); }
  .card--back .brand { left: 40px; top: 110px; font-size: 24px; color: var(--tan); }
  .card--back .brand__dot { background: var(--tan); }
  .web { position: absolute; left: 60px; top: 210px; font-size: 15px; color: var(--tan-soft); }
  .person { position: absolute; left: 330px; top: 60px; }
  .person__name { font-size: 24px; font-weight: 600; line-height: 1.1; }
  .person__title { font-size: 11px; color: var(--tan-soft); }
  .contacts { position: absolute; left: 330px; top: 130px; list-style: none; font-size: 15px; line-height: 1.45; }
  .contacts li { display: flex; align-items: flex-start; gap: 10px; }
  .contacts svg { width: 12px; height: 12px; margin-top: 5px; flex: none; fill: var(--tan); }
  .contacts .indent { padding-left: 22px; }
</style>
</head>
<body>
<main class="stage">
  <section class="card card--front" role="img" aria-label="Warm natural wood grain card face with company name">
    <div class="brand"><span class="brand__dot"></span>R.T. Custom Cabinets</div>
  </section>

  <section class="card card--back">
    <div class="brand"><span class="brand__dot"></span>R.T. Custom Cabinets</div>
    <p class="web">www.rtcustomcabinets.example</p>

    <div class="person">
      <p class="person__name">Name Here</p>
      <p class="person__title">Title Here</p>
    </div>

    <ul class="contacts">
      <li><svg viewBox="0 0 12 12"><rect x="3" y="0" width="6" height="12" rx="1"/></svg>604-555-0173</li>
      <li><svg viewBox="0 0 12 12"><path d="M1 4c3-3 7-3 10 0l-2 2-1.5-1V4h-3v1L3 6z"/><rect x="2" y="7" width="8" height="4" rx="1"/></svg>604-555-0173</li>
      <li><svg viewBox="0 0 12 12"><rect x="0" y="4" width="12" height="7" rx="1"/><rect x="3" y="1" width="6" height="3"/></svg>604-555-0173</li>
      <li><svg viewBox="0 0 12 12"><circle cx="6" cy="6" r="6"/><path d="M3 6l2 2 4-4" stroke="#2a160d" stroke-width="1.5" fill="none"/></svg>info@rtcustomcabinets.example</li>
      <li><svg viewBox="0 0 12 12"><path d="M6 0a4 4 0 0 1 4 4c0 3-4 8-4 8S2 7 2 4a4 4 0 0 1 4-4z"/></svg>5826 Larkspur Avenue</li>
      <li class="indent">Burnaby, B.C. V7K 2P9</li>
    </ul>
  </section>
</main>
</body>
</html>
```